Membership card Design

Hi I need a new membership card design for a social University club located in New Zealand. Our club name is called Maple Crest Society (MCSOC) and we provide a social hub for international students from Asia to meet local students. We are a non-profit organization that organizes activities such as paintball, ski trips, parties and day trips for our members. We need designs that look more like a membership card than a name card because we will be giving them to our members as a proof of membership. We would prefer a design that is simple in the front and with our club details, contacts and a place to write down a membership number on the back. We would like our card to have designs using the colours red, black, grey and orange. The design must incoporate the logo attached in this project. If possible, we would like the flower in the Hong Kong Flag to be incoporated in the design. The final design must look more like a membership card than a name card and communicate professionalism and high quality.

Target Market(s)

University Students

Industry/Entity Type

Non-Profit

Requirements
Must have
• The design must include:

The logo of our club
Our facebook page details: www.friendspage.example/maplecrest.soc
Our email: maplecrestsoc@mailbox.example
A place behind the card to print membership numbers.

```html
<!DOCTYPE html>
<html lang="en">
<head>
<meta charset="utf-8">
<title>Maple Crest Society – Membership Card</title>
<link rel="stylesheet" href="https://fonts.googleapis.com/css2?family=Crimson+Text:wght@400;700&display=swap">
<style>
  :root {
    --sheet: #ffffff;
    --frame: #111111;
    --front: #48484a;
    --front-emblem: #545456;
    --back: #efefef;
    --back-emblem: #e6e6e6;
    --red: #e0201f;
    --ink-soft: #7a7a7a;
  }
  html, body {
    margin: 0;
    padding: 0;
    width: 947px;
    height: 1200px;
    overflow: hidden;
    background: var(--sheet);
  }
  .sheet {
    position: relative;
    width: 947px;
    height: 1200px;
    font-family: "Crimson Text", Georgia, serif;
  }
  .sheet-frame {
    position: absolute;
    left: 10px;
    top: 10px;
    width: 923px;
    height: 1176px;
    border: 2px solid var(--frame);
  }
  .card {
    position: absolute;
    left: 95px;
    width: 755px;
    height: 473px;
    border-radius: 46px;
    overflow: hidden;
  }
  .card-front { top: 85px; background: var(--front); }
  .card-back { top: 638px; background: var(--back); }

  .emblem {
    position: absolute;
    border-radius: 50%;
  }
  .card-front .emblem {
    left: 395px;
    top: 55px;
    width: 330px;
    height: 330px;
    background: var(--front-emblem);
  }
  .card-back .emblem {
    left: 25px;
    top: 75px;
    width: 320px;
    height: 320px;
    background: var(--back-emblem);
  }

  .brand-mark {
    position: absolute;
    left: 240px;
    top: 182px;
    width: 96px;
    height: 96px;
    border-radius: 50%;
    background: var(--red);
  }
  .club-name {
    position: absolute;
    right: 26px;
    top: 290px;
    margin: 0;
    color: var(--red);
    font-weight: 400;
    font-size: 80px;
    font-variant: small-caps;
    letter-spacing: 3px;
    line-height: 1;
    white-space: nowrap;
  }
  .card-title {
    position: absolute;
    right: 24px;
    top: 374px;
    margin: 0;
    color: var(--red);
    font-weight: 700;
    font-size: 25px;
    line-height: 1;
  }

  .field-label {
    position: absolute;
    margin: 0;
    color: var(--red);
    font-weight: 700;
    font-size: 23px;
    line-height: 1;
  }
  .field-name { left: 433px; top: 58px; }
  .field-number { left: 391px; top: 186px; }
  .field-line {
    position: absolute;
    height: 0;
    border-top: 1.5px dotted var(--red);
  }
  .line-name { left: 333px; width: 385px; top: 123px; }
  .line-number { left: 329px; width: 385px; top: 250px; }

  .contact {
    position: absolute;
    left: 323px;
    display: flex;
    align-items: center;
    gap: 10px;
    color: var(--ink-soft);
    font-size: 23px;
    line-height: 1;
    white-space: nowrap;
  }
  .contact-page { top: 328px; }
  .contact-mail { top: 374px; }
  .page-dot {
    width: 18px;
    height: 18px;
    border-radius: 50%;
    background: var(--ink-soft);
    margin-left: 4px;
  }
  .mail-icon { width: 28px; height: 20px; }
</style>
</head>
<body>
<main class="sheet">
  <div class="sheet-frame"></div>

  <section class="card card-front" aria-label="Membership card front">
    <div class="emblem" aria-hidden="true"></div>
    <div class="brand-mark" aria-hidden="true"></div>
    <h1 class="club-name">Maple Crest Soc</h1>
    <p class="card-title">Membership Card</p>
  </section>

  <section class="card card-back" aria-label="Membership card back">
    <div class="emblem" aria-hidden="true"></div>
    <p class="field-label field-name">Member Name</p>
    <div class="field-line line-name"></div>
    <p class="field-label field-number">Membership Number</p>
    <div class="field-line line-number"></div>

    <div class="contact contact-page">
      <span class="page-dot"></span>
      <span>www.friendspage.example/maplecrest.soc</span>
    </div>
    <div class="contact contact-mail">
      <svg class="mail-icon" viewBox="0 0 28 20" aria-hidden="true">
        <rect x="1" y="1" width="26" height="18" fill="none" stroke="#7a7a7a" stroke-width="1.6"/>
        <polyline points="1,1 14,12 27,1" fill="none" stroke="#7a7a7a" stroke-width="1.6"/>
      </svg>
      <span>maplecrestsoc@mailbox.example</span>
    </div>
  </section>
</main>
</body>
</html>
```